Life Coaching Business - needs business card design with logo

I need a business card and logo design for a life coaching business I started based in Los Angeles. I offer services to clients that wish to bring more balance and overall wholeness to their lives. As of right now, the business name is "Marcus Elwood Coaching." An iidea I had for the logo was to be kind of a Yin-Yang symbol but with dolphins, as the dolphin has symbolic meaning for my business. Although I am really open to other ideas as long as it incorporates the idea of “balance,” “wholeness,” and “dolphins.”I also wanted to incorporate the color blue, maybe in the form of water, waves, or some sort of peaceful imagery.

```html
<!DOCTYPE html>
<html lang="en">
<head>
<meta charset="utf-8">
<title>Marcus Elwood Coaching – Business Card</title>
<link rel="stylesheet" href="https://fonts.googleapis.com/css2?family=Montserrat:wght@800&family=EB+Garamond:wght@400&display=swap">
<style>
  :root {
    --backdrop: #93bdf8;
    --card-white: #ffffff;
    --wave-blue: #2e86c6;
    --deep-blue: #0f6ccc;
    --mist-grey: #bdbdbd;
    --ink-grey: #7a7a7a;
    --ink-dark: #1c1c1c;
  }
  html, body {
    margin: 0;
    width: 1200px;
    height: 1200px;
    overflow: hidden;
    background: var(--backdrop);
  }
  .canvas {
    width: 1200px;
    height: 1200px;
    display: flex;
    flex-direction: column;
    align-items: center;
    justify-content: center;
    gap: 80px;
  }
  .card {
    position: relative;
    width: 900px;
    height: 500px;
    border-radius: 36px;
    overflow: hidden;
    background: var(--card-white);
    box-shadow: 0 10px 24px rgba(30, 70, 130, 0.25);
  }
  .card svg.card-art {
    position: absolute;
    inset: 0;
    width: 100%;
    height: 100%;
  }
  .wave-blue { fill: var(--wave-blue); }
  .deep-blue { fill: var(--deep-blue); }
  .mist-grey { fill: var(--mist-grey); }
  .white { fill: var(--card-white); }

  /* Front */
  .brand {
    position: absolute;
    left: 190px;
    top: 190px;
    display: flex;
    align-items: center;
    gap: 24px;
  }
  .brand-dot {
    width: 110px;
    height: 110px;
    border-radius: 50%;
    background: var(--wave-blue);
    flex: none;
  }
  .brand-name {
    font-family: "Montserrat", sans-serif;
    font-weight: 800;
    color: var(--ink-grey);
    line-height: 1;
    text-transform: uppercase;
  }
  .brand-name .line-1 { display: block; font-size: 30px; letter-spacing: 1px; }
  .brand-name .line-2 { display: block; font-size: 50px; letter-spacing: 1px; margin-top: 4px; }

  /* Back */
  .contact-list {
    position: absolute;
    right: 390px;
    top: 120px;
    margin: 0;
    padding: 0;
    list-style: none;
    font-family: "EB Garamond", serif;
    font-size: 34px;
    color: var(--ink-dark);
    text-align: right;
  }
  .contact-list li {
    display: flex;
    align-items: center;
    justify-content: flex-end;
    gap: 18px;
    margin-bottom: 26px;
  }
  .contact-list svg { width: 34px; height: 34px; flex: none; }
  .back-name {
    position: absolute;
    right: 40px;
    top: 300px;
    width: 160px;
    font-family: "Montserrat", sans-serif;
    font-weight: 800;
    font-size: 24px;
    line-height: 1.2;
    color: var(--card-white);
    text-transform: uppercase;
    letter-spacing: 0.5px;
    text-align: center;
  }
  .back-name span { display: block; }
</style>
</head>
<body>
<main class="canvas">

  <section class="card card-front" aria-label="Business card front">
    <svg class="card-art" viewBox="0 0 900 500" preserveAspectRatio="none" aria-hidden="true">
      <path class="mist-grey" d="M560 60 C680 20 820 30 900 80 L900 60 C800 10 660 20 560 60 Z"/>
      <path class="wave-blue" d="M470 130 C620 40 860 40 900 140 L900 500 L330 500 C560 470 800 400 830 260 C850 140 640 90 470 130 Z"/>
      <path class="mist-grey" d="M0 180 C60 260 160 300 300 330 C160 320 60 290 0 240 Z"/>
      <path class="deep-blue" d="M0 280 C120 350 320 400 600 420 C340 430 120 400 0 360 Z"/>
      <path class="wave-blue" d="M0 380 C150 440 300 470 420 500 L0 500 Z"/>
    </svg>
    <div class="brand">
      <span class="brand-dot"></span>
      <span class="brand-name">
        <span class="line-1">Marcus Elwood</span>
        <span class="line-2">Coaching</span>
      </span>
    </div>
  </section>

  <section class="card card-back" aria-label="Business card back">
    <svg class="card-art" viewBox="0 0 900 500" preserveAspectRatio="none" aria-hidden="true">
      <rect class="wave-blue" x="0" y="0" width="900" height="500"/>
      <path class="mist-grey" d="M0 0 L620 0 C720 120 720 330 560 420 C380 500 150 480 0 470 Z"/>
      <path class="deep-blue" d="M0 0 L600 0 C700 120 700 320 540 400 C370 480 150 460 0 450 Z"/>
      <path class="white" d="M0 0 L560 0 C680 110 680 300 520 380 C360 450 150 440 0 420 Z"/>
      <path class="wave-blue" d="M590 40 C660 120 670 260 600 330 C640 250 640 130 590 40 Z"/>
    </svg>
    <ul class="contact-list">
      <li>0123456789
        <svg viewBox="0 0 24 24"><circle cx="12" cy="12" r="12" fill="var(--wave-blue)"/><path d="M9 6 C6 8 7 14 12 17 C14 18 16 18 17 16 L15 14 L13 15 C11 14 10 12 10 10 L11 9 Z" fill="#fff"/></svg>
      </li>
      <li>email
        <svg viewBox="0 0 24 24"><rect x="1" y="5" width="22" height="14" fill="var(--wave-blue)"/><path d="M2 6 L12 13 L22 6" stroke="#fff" stroke-width="1.8" fill="none"/></svg>
      </li>
      <li>address
        <svg viewBox="0 0 24 24"><path d="M12 2 C7 2 4 6 4 10 C4 15 12 22 12 22 C12 22 20 15 20 10 C20 6 17 2 12 2 Z" fill="var(--wave-blue)"/><circle cx="12" cy="10" r="3" fill="#fff"/></svg>
      </li>
    </ul>
    <div class="back-name"><span>Marcus</span><span>Elwood</span><span>Coaching</span></div>
  </section>

</main>
</body>
</html>
```